依頼詳細
ダウンロードデータ内にサイトマップとデザイン制作要望を準備しています。
現行サイトURLはデータ内でご確認ください。

◆サイトマップ
1.TOP
└2.当サロンについて
└3.初めての方へ
└4.頭皮・髪質改善へのこだわり
└5.髪質のお悩み
└6.カラーダメージのお悩み
└7.頭皮のお悩み
└8.お悩みビフォー・アフター
└9.VORA公式アプリ
└10.Q&A
└11.MENU・COUPON
└12.PRODUCT
└13.STAFF(一覧)
└14.VOICE(一覧)
└15.NEWS・BLOG(一覧)
└16.RECRUIT
└17.CONTACT

◆希望デザインカラー
希望テイストに合わせて色を使用いただきたいですが、すべて茶系・モノクロなど暗いイメージにならないようにゴールドや明るい色をポイントで使用いただきたいです。

◆デザインのテイスト・イメージ
・高級感(上品な高級感)
・清潔
・見やすさのユーザビリティとお洒落さを取り入れたデザイン

◆参考イメージ
https://beautyroom-marnel-example.com/
①ターゲット層に好まれるデザインだと感じました。
(色の配色、キラキラした背景やグラデーションのバランス)
②コンテンツ毎にデザインが異なり、目に止まりやすいと感じました。
③文章量がちょうど良く、直感的に内容を把握できる
(同じくらいの文章量・余白を希望します)
明るくデザインに映える色をポイントで使用
• イラストレーター形式 (.ai)
• フォトショップ形式 (.psd)
【素材・データ】
①制作要望・素材写真
制作要望・素材写真について、下記よりダウンロードしてご使用ください。
https://filedepot-sample.jp/download/9a1c7e5b20d84f36a0be7c1d92f4e6a8b3c5d7f1
ダウンロードパスワード q8wm2tv6
また、現行サイトの素材や内容を使用頂いても問題ありません。
ロゴは現行サイトから使用下さい。

②写真(その他)
Pictora Bank[ https://images.pictorabank-sample.com/jp/]で定期契約をしています。
また定期契約のものは弊社の負担となり、ランサー様に負担はありません。
カンプ画像を入れてください。
その際、通常アセットで購入できる画像でお願いいたします。

③その他
・業務への支障がでる可能性がございますので、店舗へ直接の連絡はお控え下さい。
・申し訳ございませんがXD形式の納品はお受けできかねます。
・デザインの横幅は1300pxで作成お願いいたします。
どうぞ自由な発想でご提案ください。

```html
<!DOCTYPE html>
<html lang="ja">
<head>
<meta charset="utf-8">
<title>VORA | オトナ女性のためのお悩み解決サロン</title>
<link rel="stylesheet" href="https://fonts.googleapis.com/css2?family=Noto+Serif+JP:wght@400;500;600&family=Cormorant+Garamond:ital,wght@0,400;0,500;1,400&display=swap">
<style>
:root{
  --ink:#3b3431;
  --ink-soft:#6d625c;
  --gold-1:#b08c45;
  --gold-2:#d9c084;
  --gold-line:#c9ad6c;
  --cream:#fbf8f3;
  --blush:#f6ebe6;
  --line:#d9cfc4;
  --white:#ffffff;
}
*{box-sizing:border-box;margin:0;padding:0}
html,body{width:1200px;height:4308px;overflow:hidden}
body{position:relative;background:var(--white);color:var(--ink);font-family:"Noto Serif JP",serif;}
.abs{position:absolute}
.logo{font-family:"Cormorant Garamond",serif;font-weight:500;letter-spacing:.18em;color:var(--ink)}
.btn-gold{display:flex;align-items:center;justify-content:center;background:linear-gradient(90deg,var(--gold-1),var(--gold-2) 50%,var(--gold-1));color:var(--white);font-size:15px;letter-spacing:.1em}
.heading{width:100%;text-align:center;font-size:34px;font-weight:500;letter-spacing:.12em}
.heading-en{font-family:"Cormorant Garamond",serif;font-size:42px;font-weight:400}

/* header */
.site-header{left:0;top:0;width:1200px;height:120px;background:var(--white)}
.site-header .logo{left:150px;top:22px;font-size:32px;line-height:1}
.global-nav{left:155px;top:84px;display:flex;gap:46px;font-size:14px;line-height:1}
.header-actions{right:60px;top:28px;display:flex;gap:14px}
.header-actions .btn-gold{width:120px;height:36px;font-size:13px}
.tel-btn{width:148px;height:36px;border:1px solid var(--gold-line);display:flex;align-items:center;justify-content:center;font-size:13px;color:var(--gold-1)}

/* hero */
.hero{left:0;top:120px;width:1200px;height:680px;background:linear-gradient(120deg,#f1e8dc,#e6d9c7 45%,#cbb89c 75%,#f3ede4)}
.hero-copy{left:30px;top:250px;font-size:40px;line-height:1.65;letter-spacing:.1em;color:var(--white);text-shadow:0 0 14px rgba(90,70,50,.35)}

/* intro */
.intro-title{top:880px;line-height:1.7}
.intro-text{left:300px;top:1036px;width:600px;text-align:center;font-size:14px;line-height:1.9;color:var(--ink-soft)}
.intro-text p+p{margin-top:16px}
.intro-btn{top:1384px;width:260px;height:44px}

/* news */
.news-title{top:1510px}
.news-box{left:300px;top:1612px;width:600px;height:250px;border:1px solid var(--line);padding:10px 46px}
.news-item{border-bottom:1px solid var(--line);padding:14px 0;font-size:14px}
.news-item:last-child{border-bottom:0}
.news-date{display:block;font-family:"Cormorant Garamond",serif;font-size:14px;color:var(--ink-soft);margin-bottom:6px}

/* treatment */
.tech-title{top:1960px}
.tech-label{width:260px;text-align:center;font-size:20px;letter-spacing:.08em}
.tech-photo{border-radius:50%;width:224px;height:224px}
.tech-btn{width:224px;height:40px}
.tech-text{left:300px;top:2510px;width:600px;text-align:center;font-size:15px;line-height:2.1;color:var(--ink-soft)}

/* menu & style */
.info-band{left:0;top:2800px;width:1200px;height:400px;background:var(--blush)}
.info-card{width:300px}
.info-photo{width:300px;height:190px}
.info-body{background:var(--white);height:170px;padding:14px 22px;font-size:12px;line-height:1.8}
.info-body h3{font-family:"Cormorant Garamond",serif;font-weight:400;font-size:22px;line-height:1.3;margin-bottom:4px}
.info-body .btn-gold{width:150px;height:32px;font-size:12px;margin:10px auto 0}

/* staff */
.staff-title{top:3320px}
.staff{width:176px;text-align:center;font-size:14px}
.staff-photo{width:176px;height:180px;border:6px solid #efe3cf;margin-bottom:12px}
.staff-btn{left:470px;top:3668px;width:260px;height:40px}

/* banners */
.banner{width:380px;height:240px;border:8px solid #f1e4d6;display:flex;align-items:center;justify-content:center;font-family:"Cormorant Garamond",serif;font-style:italic;font-size:54px;letter-spacing:.12em;color:var(--white);text-shadow:0 0 10px rgba(120,90,60,.5)}

/* footer */
.site-footer{left:0;top:4080px;width:1200px;height:228px;background:var(--cream)}
.site-footer .logo{left:230px;top:28px;font-size:48px;line-height:1}
.sns{left:270px;top:110px;display:flex;gap:16px}
.sns span{width:28px;height:28px;border-radius:50%;background:var(--ink-soft)}
.footer-info{left:480px;top:36px;width:330px;font-size:12px;line-height:1.9;color:var(--ink-soft)}
.footer-info strong{font-size:14px;color:var(--ink);font-weight:500}
.footer-reserve{left:840px;top:40px;width:200px;height:38px;font-size:13px}
.store-badges{left:840px;top:100px;display:flex;gap:14px}
.store-badges span{width:92px;height:30px;border-radius:6px;background:var(--ink)}
.copyright{left:0;top:200px;width:1200px;text-align:center;font-size:10px;color:var(--ink-soft)}
</style>
</head>
<body>

<header class="site-header abs">
  <div class="logo abs">VORA</div>
  <nav class="global-nav abs">
    <span>VORAについて</span><span>こだわり</span><span>メニュー</span><span>スタッフ</span><span>お客様の声</span><span>よくあるご質問</span><span>求人情報</span>
  </nav>
  <div class="header-actions abs">
    <div class="btn-gold">WEB予約</div>
    <div class="tel-btn">TEL : 000-0000-0000</div>
  </div>
</header>

<section class="hero abs" role="img" aria-label="観葉植物とロゴ看板が置かれた明るいサロン店内の写真">
  <h1 class="hero-copy abs" style="font-weight:500">オトナ女性のための<br>お悩み解決サロン</h1>
</section>

<section>
  <h2 class="heading intro-title abs">悩みを抱える<br>オトナ女性のための美容院</h2>
  <div class="intro-text abs">
    <p>年齢を重ねるほど増えていく、<br>「髪が細い、広がる」「髪の艶&#12539;潤い」「白髪が目立つ」など<br>さまざまな髪や頭皮の悩みを抱えるオトナ女性のための美容院です。</p>
    <p>「髪が細くなってきた」「ボリュームが出ない」<br>「髪がまとまらない」「髪や頭皮の悩みが気になる」「パサつき」<br>など、小さな悩みでも構いません。</p>
    <p>ぜひ、当店の美容師にご相談ください。<br>「似合う髪型」を一緒に探していきます。</p>
    <p>スタッフ一同、心よりお客様のご来店をお待ちしております。</p>
  </div>
  <div class="btn-gold intro-btn abs" style="left:320px">初めての方へ</div>
  <div class="btn-gold intro-btn abs" style="left:620px">こだわりについて</div>
</section>

<section>
  <h2 class="heading heading-en news-title abs">News</h2>
  <div class="news-box abs">
    <div class="news-item"><span class="news-date">2021.06.01</span>ホームページをリニューアルしました</div>
    <div class="news-item"><span class="news-date">2021.06.15</span>営業時間のお知らせ</div>
    <div class="news-item"><span class="news-date">2021.06.28</span>新商品が入荷しました</div>
  </div>
</section>

<section>
  <h2 class="heading tech-title abs">VORAの術</h2>
  <div class="tech-label abs" style="left:170px;top:2036px">髪質のお悩み</div>
  <div class="tech-photo abs" style="left:188px;top:2080px;background:linear-gradient(135deg,#8a5a3e,#c89a72)" role="img" aria-label="髪の毛先を手に取る写真"></div>
  <div class="btn-gold tech-btn abs" style="left:188px;top:2316px">詳しく見る</div>

  <div class="tech-label abs" style="left:470px;top:2116px">頭皮のお悩み</div>
  <div class="tech-photo abs" style="left:488px;top:2184px;background:linear-gradient(135deg,#e8ddd2,#b9a895)" role="img" aria-label="ヘッドスパ施術中の写真"></div>
  <div class="btn-gold tech-btn abs" style="left:488px;top:2424px">詳しく見る</div>

  <div class="tech-label abs" style="left:770px;top:2036px">カラーダメージのお悩み</div>
  <div class="tech-photo abs" style="left:788px;top:2080px;background:linear-gradient(135deg,#2f2724,#8b7a70)" role="img" aria-label="カラー施術中の髪の写真"></div>
  <div class="btn-gold tech-btn abs" style="left:788px;top:2316px">詳しく見る</div>

  <p class="tech-text abs">「髪が細い、広がる」「髪の艶&#12539;潤い」「白髪が目立つ」など<br>さまざまなオトナ女性の悩みに対し、VORA独自の技術で<br>「ツヤとハリ」を「ずっと」お届けすることを<br>実現しております。</p>
  <div class="btn-gold abs" style="left:460px;top:2676px;width:280px;height:44px">技術&#12539;施術事例はこちら</div>
</section>

<section class="info-band abs">
  <div class="info-card abs" style="left:220px;top:24px">
    <div class="info-photo" style="background:linear-gradient(135deg,#f2e9dd,#d9c7ad)" role="img" aria-label="サロンの施術スペースの写真"></div>
    <div class="info-body">
      <h3>Menu</h3>
      カット&#12539;&#12539;&#12539;&#12539;&#12539;&#12539;&#12539;&#12539;&#12539;&#12539;&#12539;&#12539;&#165;5,000円<br>
      カラー&#12539;&#12539;&#12539;&#12539;&#12539;&#12539;&#12539;&#12539;&#12539;&#12539;&#12539;&#165;6,000円<br>
      トリートメント&#12539;&#12539;&#12539;&#12539;&#12539;&#12539;&#12539;&#165;4,000円
      <div class="btn-gold">メニュー一覧</div>
    </div>
  </div>
  <div class="info-card abs" style="left:672px;top:24px">
    <div class="info-photo" style="background:linear-gradient(135deg,#e4d8cf,#8f7a6c)" role="img" aria-label="ヘアスタイル例の写真"></div>
    <div class="info-body">
      <h3>Style</h3>
      丁寧なカウンセリングとスタイルで<br>理想の髪型を実現します。
      <div class="btn-gold" style="margin-top:32px">ヘアスタイル一覧</div>
    </div>
  </div>
</section>

<section>
  <h2 class="heading staff-title abs">スタッフ</h2>
  <div class="staff abs" style="left:152px;top:3408px"><div class="staff-photo" style="background:linear-gradient(135deg,#d6c3ad,#7a6555)" role="img" aria-label="スタッフの写真"></div>森川 悠真</div>
  <div class="staff abs" style="left:400px;top:3408px"><div class="staff-photo" style="background:linear-gradient(135deg,#e3d6c6,#9d8672)" role="img" aria-label="スタッフの写真"></div>高瀬 美咲</div>
  <div class="staff abs" style="left:640px;top:3408px"><div class="staff-photo" style="background:linear-gradient(135deg,#c9a27e,#6a4a38)" role="img" aria-label="スタッフの写真"></div>小野 綾香</div>
  <div class="staff abs" style="left:872px;top:3408px"><div class="staff-photo" style="background:linear-gradient(135deg,#efe6dc,#a89584)" role="img" aria-label="スタッフの写真"></div>水野 彩花</div>
  <div class="btn-gold staff-btn abs">スタッフ一覧</div>
</section>

<section>
  <div class="banner abs" style="left:180px;top:3800px;background:linear-gradient(135deg,#f4ede6,#dccdc0)" role="img" aria-label="お客様の声バナーの背景写真">VOICE</div>
  <div class="banner abs" style="left:640px;top:3800px;background:linear-gradient(135deg,#f3e6d3,#cbb08a)" role="img" aria-label="ヘアケア商品が並ぶ写真">PRODUCT</div>
</section>

<footer class="site-footer abs">
  <div class="logo abs">VORA</div>
  <div class="sns abs"><span></span><span></span></div>
  <div class="footer-info abs">
    <strong>髪質改善 頭皮ケア美容室 VORA</strong><br>
    〒000-0000 東市見原町1丁目2-3<br>
    TEL : 000-0000-0000<br>
    【平日】10:00-19:00 【土日祝】9:00-18:00<br>
    【定休日】毎週火曜日
  </div>
  <div class="btn-gold footer-reserve abs">WEB予約</div>
  <div class="store-badges abs"><span></span><span></span></div>
  <div class="copyright abs">&#169; VORA hair salon. All Rights Reserved.</div>
</footer>

</body>
</html>
```